My Business is Car Dealership, we sale cars and trucks, I’m looking for a sign design
I need 2 signage
9ā€ by 7ā€ feet.
the other sign is 3" feet high and the width is 12" feet

For further reference about the company , you can check my website
www.harrowbayautosale.com

Industry/Entity Type

Business

Requirements
Must have
• picture of 2018 marlo K240 or 2018 Vantrelle Duskmoor
Nice to have
• the business name Harrow Bay Auto Sale visible from far distance

```html
<!DOCTYPE html>
<html lang="en">
<head>
<meta charset="utf-8">
<title>Harrow Bay Auto Sale — 9×7 ft sign</title>
<link href="https://fonts.googleapis.com/css2?family=Racing+Sans+One&family=Montserrat:wght@500;600;700&display=swap" rel="stylesheet">
<style>
  :root {
    --page: #ffffff;
    --board: #050505;
    --red: #e2151f;
    --white: #ffffff;
    --grey: #a9a9a9;
    --car-red: #d8232a;
    --car-dark: #2a0b0d;
  }
  html, body {
    margin: 0;
    width: 1200px;
    height: 1200px;
    overflow: hidden;
    background: var(--page);
  }
  .sign {
    position: absolute;
    left: 100px;
    top: 211px;
    width: 1000px;
    height: 778px;
    background: var(--board);
    overflow: hidden;
  }
  .brand-mark {
    position: absolute;
    left: 38px;
    top: 50px;
    width: 164px;
    height: 164px;
    box-sizing: border-box;
    border-radius: 50%;
    border: 7px solid var(--red);
  }
  .brand {
    position: absolute;
    margin: 0;
    font-family: "Racing Sans One", sans-serif;
    font-weight: 400;
    line-height: 1;
    white-space: nowrap;
    text-align: center;
  }
  .brand-name {
    top: 22px;
    left: 230px;
    width: 740px;
    font-size: 126px;
    color: var(--red);
  }
  .brand-line {
    top: 120px;
    left: 280px;
    width: 600px;
    font-size: 116px;
    color: var(--white);
  }
  .vehicle {
    position: absolute;
    left: 114px;
    top: 228px;
    width: 750px;
    height: 340px;
    border-radius: 40px;
    background: radial-gradient(ellipse at 50% 50%, var(--car-red) 0%, #a8141a 55%, var(--car-dark) 100%);
  }
  .tagline, .phone, .web {
    position: absolute;
    left: 0;
    width: 1000px;
    text-align: center;
    font-family: "Montserrat", sans-serif;
    white-space: nowrap;
    margin: 0;
  }
  .tagline {
    top: 578px;
    font-size: 29px;
    font-weight: 500;
    letter-spacing: 6px;
    color: var(--grey);
  }
  .phone {
    top: 604px;
    font-size: 110px;
    font-weight: 700;
    letter-spacing: 2px;
    color: var(--white);
    line-height: 1.1;
  }
  .web {
    top: 718px;
    font-size: 25px;
    font-weight: 700;
    letter-spacing: 15.5px;
    color: var(--white);
  }
  .web .accent { color: var(--red); }
</style>
</head>
<body>
  <main class="sign">
    <div class="brand-mark" aria-hidden="true"></div>

    <h1 class="brand brand-name">Harrow Bay</h1>
    <p class="brand brand-line">Auto Sale</p>

    <div class="vehicle" role="img" aria-label="Photo of a red sports coupe with black racing stripes, front three-quarter view"></div>

    <p class="tagline">we buy your car or truck for cash</p>
    <p class="phone">831-555-0142</p>
    <p class="web">www.<span class="accent">harrow</span>bay<span class="accent">auto</span>sale<span class="accent">.com</span></p>
  </main>
</body>
</html>
```